Quorbanil Business Cards & Stationery Design
Business Cards & Stationery Design
Quorbanil Business Cards & Stationery Design - Information Technology
Creative Brief
Professional
Neville Prothick
Technical Consultant
47 marbury close fenwick NSW 2012 Australia
nprothick@quorbanil.example
http://www.quorbanil.example
The font used is called Aller, and can be downloaded from : http://www.glyphmerrow.example/buyonline/fonts/aller
www.quorbanil.example

```html
<!DOCTYPE html>
<html lang="en">
<head>
<meta charset="utf-8">
<title>Quorbanil Stationery</title>
<link href="https://fonts.googleapis.com/css2?family=Ubuntu:wght@400;500;700&display=swap" rel="stylesheet">
<style>
:root{
  --bg:#e8e4de;
  --paper:#ffffff;
  --ink:#3a3a3a;
  --muted:#8a8a8a;
  --green:#1f8a2c;
  --green-light:#6fbf4a;
  --black:#141414;
  --faint:#eef4ea;
  --rule:#c9c9c9;
}
*{margin:0;padding:0;box-sizing:border-box}
html,body{width:1200px;height:463px;overflow:hidden;background:var(--bg)}
body{position:relative;font-family:"Ubuntu",sans-serif;color:var(--ink)}
.piece{position:absolute;background:var(--paper);box-shadow:0 2px 6px rgba(0,0,0,.18);overflow:hidden}
.band{position:absolute;left:0;right:0;bottom:0;background:var(--green)}
.band::after{content:"";position:absolute;left:0;right:0;top:-3px;height:3px;background:var(--black)}
.logo{display:flex;align-items:center;gap:6px}
.logo-mark{background:var(--green);flex:none}
.logo-name{font-weight:500;color:var(--ink);letter-spacing:-.5px}
.logo-stack{flex-direction:column;gap:4px}
.deco{position:absolute;background:var(--faint)}

/* business cards */
.card{left:7px;width:204px;height:120px}
.card-info{top:12px}
.card-info .logo{position:absolute;left:12px;top:14px}
.card-info .logo-mark{width:14px;height:14px}
.card-info .logo-name{font-size:13px}
.contact{position:absolute;left:104px;top:10px;font-size:5.6px;line-height:8px;color:var(--muted)}
.contact .person{font-size:7.5px;color:var(--ink);font-weight:500;line-height:9px}
.contact .role{margin-bottom:4px}
.card-info .band{height:6px}
.card-logo{top:154px}
.card-logo .logo{position:absolute;left:14px;top:40px}
.card-logo .logo-mark{width:26px;height:26px}
.card-logo .logo-name{font-size:30px}
.card-logo .band{height:8px}
.card-dark{top:298px;background:var(--black)}
.card-dark .logo{position:absolute;left:0;right:0;top:40px;justify-content:center}
.card-dark .logo-mark{width:14px;height:14px}
.card-dark .logo-name{font-size:15px;color:#fff}
.card-dark .web{position:absolute;left:0;right:0;top:70px;text-align:center;font-size:6px;color:#bdbdbd}
.card-dark .band{height:5px}
.card-dark .band::after{display:none}

/* letterhead & fax */
.sheet{top:12px;width:294px;height:439px}
.letterhead{left:223px}
.fax{left:536px}
.sheet .logo{position:absolute;left:0;right:0;top:30px;justify-content:center}
.sheet .logo-mark{width:22px;height:22px}
.sheet .logo-name{font-size:27px}
.sheet .deco{right:-40px;bottom:30px;width:190px;height:190px;transform:rotate(45deg)}
.sheet-footer{position:absolute;left:0;right:0;bottom:16px;text-align:center;font-size:4.6px;color:var(--muted)}
.sheet .band{height:6px}
.fax-title{position:absolute;right:16px;top:62px;font-size:17px;font-weight:700}
.fax-table{position:absolute;left:12px;right:12px;top:84px;border-collapse:collapse;font-size:4.8px;color:var(--muted)}
.fax-table td{border:1px solid var(--rule);height:10px;padding:0 3px}
.fax-table .label{width:34px;background:#f3f3f3}
.fax-options{position:absolute;left:12px;top:133px;display:flex;gap:14px;font-size:4.6px;color:var(--muted)}
.fax-options span::before{content:"";display:inline-block;width:4px;height:4px;border:1px solid var(--rule);margin-right:2px;vertical-align:-1px}

/* compliment slip */
.slip{left:850px;top:12px;width:343px;height:192px}
.slip .logo{position:absolute;left:16px;top:14px}
.slip .logo-mark{width:14px;height:14px}
.slip .logo-name{font-size:13px}
.slip .tagline{position:absolute;left:16px;top:34px;font-size:5px;color:var(--muted)}
.slip .deco{right:-20px;bottom:6px;width:120px;height:120px;transform:rotate(45deg)}
.slip .band{height:6px}

/* envelope */
.envelope{left:850px;top:240px;width:343px;height:192px}
.envelope svg{position:absolute;inset:0}
.envelope .logo{position:absolute;left:0;right:0;top:40px;justify-content:center}
.envelope .logo-mark{width:18px;height:18px}
.envelope .logo-name{font-size:16px;color:#fff}
</style>
</head>
<body>

<section class="piece card card-info">
  <div class="logo"><span class="logo-mark"></span><span class="logo-name">quorbanil</span></div>
  <div class="contact">
    <div class="person">Neville Prothick</div>
    <div class="role">Technical Consultant</div>
    <div>T +61 2 5550 0142</div>
    <div>M +61 4 5550 0187</div>
    <div>F +61 2 5550 0143</div>
    <div>47 marbury close fenwick</div>
    <div>NSW 2012 Australia</div>
    <div>nprothick@quorbanil.example</div>
    <div>www.quorbanil.example</div>
  </div>
  <div class="band"></div>
</section>

<section class="piece card card-logo">
  <div class="logo"><span class="logo-mark"></span><span class="logo-name">quorbanil</span></div>
  <div class="band"></div>
</section>

<section class="piece card card-dark">
  <div class="logo"><span class="logo-mark"></span><span class="logo-name">quorbanil</span></div>
  <div class="web">www.quorbanil.example</div>
  <div class="band"></div>
</section>

<section class="piece sheet letterhead">
  <div class="logo logo-stack"><span class="logo-mark"></span><span class="logo-name">quorbanil</span></div>
  <div class="deco"></div>
  <div class="sheet-footer">47 marbury close fenwick NSW 2012 Australia &nbsp;•&nbsp; nprothick@quorbanil.example &nbsp;•&nbsp; www.quorbanil.example</div>
  <div class="band"></div>
</section>

<section class="piece sheet fax">
  <div class="logo logo-stack"><span class="logo-mark"></span><span class="logo-name">quorbanil</span></div>
  <div class="fax-title">FAX</div>
  <table class="fax-table">
    <tr><td class="label">From</td><td></td><td class="label">To</td><td></td></tr>
    <tr><td class="label">Phone</td><td></td><td class="label">Pages</td><td></td></tr>
    <tr><td class="label">Fax</td><td></td><td class="label">Date</td><td></td></tr>
    <tr><td class="label">Re</td><td></td><td class="label">CC</td><td></td></tr>
  </table>
  <div class="fax-options"><span>Urgent</span><span>For Review</span><span>Please Comment</span><span>Please Reply</span><span>Please Recycle</span></div>
  <div class="deco"></div>
  <div class="sheet-footer">47 marbury close fenwick NSW 2012 Australia &nbsp;•&nbsp; nprothick@quorbanil.example &nbsp;•&nbsp; www.quorbanil.example</div>
  <div class="band"></div>
</section>

<section class="piece slip">
  <div class="logo"><span class="logo-mark"></span><span class="logo-name">quorbanil</span></div>
  <div class="tagline">with compliments</div>
  <div class="deco"></div>
  <div class="band"></div>
</section>

<section class="piece envelope">
  <svg width="343" height="192" viewBox="0 0 343 192" aria-hidden="true">
    <polygon points="0,0 343,0 343,14 171.5,112 0,14" fill="var(--green)"/>
    <polygon points="0,0 343,0 343,8 171.5,104 0,8" fill="var(--black)"/>
  </svg>
  <div class="logo"><span class="logo-mark"></span><span class="logo-name">quorbanil</span></div>
</section>

</body>
</html>
```